Website design for company that sells taximeters and has a taxi dispatch call center, webstore neede

Need a website with a shop with at least 20 articles, in two languages, possibly by using a purchased theme (not purchased yet).The company provides equipments and dispatch solutions for taxi companies. Typical yellow and black theme

Target Market(s)

Taxi companies

Industry/Entity Type

Taxi

Number of Pages Required

3 page

Font styles to use
Sans Serif

Colors
fbed22
000000

Requirements
Must have
• - webstore for at least 20 articles
• - Documents folder where to put pdf material related to taximeters
• - contact form message submission
Nice to have
• Feedback section
Should not have
• Blogs,

```html
<!DOCTYPE html>
<html lang="en">
<head>
<meta charset="utf-8">
<title>Contact Us – Fareline</title>
<link href="https://fonts.googleapis.com/css2?family=Open+Sans:wght@400;600;700&family=Nunito+Sans:wght@400;600;700;800&display=swap" rel="stylesheet">
<style>
:root{
  --yellow:#f2c12e;
  --yellow-soft:#f5cc45;
  --black:#0c0c0c;
  --ink:#222;
  --muted:#888;
  --line:#e6e6e6;
  --white:#fff;
}
*{box-sizing:border-box;margin:0;padding:0}
html,body{width:1200px;height:830px;overflow:hidden;background:var(--white)}
body{position:relative;font-family:"Nunito Sans",sans-serif;color:var(--ink)}
.hero{position:absolute;left:0;top:0;width:1200px;height:286px;
  background:radial-gradient(ellipse at 25% 45%,#5a2a22 0%,rgba(60,40,30,0) 30%),
  radial-gradient(ellipse at 75% 30%,#7a6a3a 0%,rgba(80,70,40,0) 40%),
  linear-gradient(180deg,#2a2620 0%,#3b352a 45%,#1a1815 80%,#0e0d0b 100%)}
.header{position:absolute;left:0;top:0;width:1200px;height:60px;color:var(--white)}
.brand{position:absolute;left:150px;top:14px;font:800 23px/1 "Nunito Sans",sans-serif;color:#f5d21c;letter-spacing:1px}
.nav{position:absolute;left:390px;top:22px;display:flex;gap:26px;list-style:none}
.nav li{font:700 12px/1 "Open Sans",sans-serif;letter-spacing:6px}
.hotline{position:absolute;left:755px;top:17px;display:flex;align-items:center;gap:10px}
.hotline span{font:600 12px/1 "Open Sans",sans-serif;color:var(--yellow);letter-spacing:2px}
.lang{position:absolute;left:889px;top:21px;font:600 10px/1 "Open Sans",sans-serif;letter-spacing:1px}
.search{position:absolute;left:982px;top:15px;width:154px;height:27px;border:2px solid var(--yellow);border-radius:14px;padding:5px 0 0 16px;font:600 12px/1 "Open Sans",sans-serif;letter-spacing:1px;color:#ddd}
.search svg{position:absolute;right:12px;top:5px}
.hero-title{position:absolute;left:0;width:1234px;top:116px;text-align:center;color:var(--white);font:700 30px/1 "Open Sans",sans-serif;letter-spacing:3px}
.crumbs{position:absolute;left:0;width:1234px;top:167px;text-align:center;color:var(--white);font:600 14px/1 "Open Sans",sans-serif;letter-spacing:1px}
.h2{position:absolute;font:400 19px/1 "Open Sans",sans-serif;color:#333;letter-spacing:.3px}
.rule{position:absolute;height:1px;background:var(--line)}
.rule::before{content:"";position:absolute;left:0;top:-1px;width:64px;height:3px;background:var(--yellow)}
.lead{position:absolute;font-size:10px;line-height:16px;color:var(--muted)}
.about{position:absolute;font-size:10px;line-height:16px;color:#333}
.label{position:absolute;font-size:9.5px;color:#555;letter-spacing:.3px}
.field{position:absolute;border:1px solid var(--line);background:var(--white)}
.send{position:absolute;left:451px;top:655px;width:146px;height:37px;border-radius:19px;background:var(--yellow-soft);color:var(--white);font:700 11.5px/37px "Nunito Sans",sans-serif;padding-left:22px}
.send svg{position:absolute;right:22px;top:11px}
.info{position:absolute;left:615px;display:flex;gap:12px;font-size:8.5px;line-height:14.5px;color:#111}
.info svg{flex:none}
.follow{position:absolute;left:615px;top:680px;font:700 12px/1 "Nunito Sans",sans-serif;color:#222}
.social{position:absolute;left:690px;top:678px;display:flex;gap:12px}
.social i{width:14px;height:14px;border-radius:50%;background:#bdbdbd;display:block}
.footer{position:absolute;left:0;top:737px;width:1200px;height:93px;background:var(--black)}
.footer .line{position:absolute;left:239px;top:42px;width:707px;height:1px;background:#555}
.legal{position:absolute;left:239px;top:53px;font-size:8px;color:var(--white)}
.legal b{color:var(--yellow);font-weight:400}
</style>
</head>
<body>
<div class="hero" role="img" aria-label="Blurred photo from inside a taxi: a lit taximeter on the dashboard with yellow cabs in traffic beyond"></div>

<header class="header">
  <div class="brand">FARELINE</div>
  <ul class="nav"><li>HOME</li><li>SHOP</li><li>CONTACT US</li></ul>
  <div class="hotline">
    <svg width="20" height="20" viewBox="0 0 24 24" fill="none" stroke="#fff" stroke-width="1.4"><path d="M5 3l4 1 1 4-2 2a12 12 0 006 6l2-2 4 1 1 4-2 2C10 21 3 14 3 5z"/><path d="M14 3a7 7 0 017 7M14 6a4 4 0 014 4"/></svg>
    <span>555.010.2200</span>
  </div>
  <div class="lang">ENG v</div>
  <div class="search">search
    <svg width="14" height="14" viewBox="0 0 16 16" fill="none" stroke="#fff" stroke-width="1.3"><circle cx="9" cy="7" r="5.5"/><path d="M5 11l-4 4"/></svg>
  </div>
</header>

<h1 class="hero-title">CONTACT US</h1>
<div class="crumbs">Home &nbsp;&gt;&nbsp; Contact Us</div>

<section class="contact-form">
  <h2 class="h2" style="left:243px;top:337px">Get in touch with Us</h2>
  <svg style="position:absolute;left:572px;top:343px" width="24" height="14" viewBox="0 0 24 14" fill="none" stroke="#f2c12e" stroke-width="1"><rect x="8" y="1" width="15" height="12"/><path d="M8 1l7.5 6L23 1M0 4h6M2 7h4M0 10h6"/></svg>
  <div class="rule" style="left:243px;top:363px;width:353px"></div>
  <p class="lead" style="left:243px;top:370px;width:350px">Lorem ipsum dolor sit amet, consectetur adipiscing elit. Vestibulum porttitor egestas orci, vitae ullamcorper risus consectetur id.</p>

  <span class="label" style="left:243px;top:419px">Full Name *</span>
  <span class="label" style="left:429px;top:419px">Your Email *</span>
  <div class="field" style="left:243px;top:433px;width:167px;height:32px"></div>
  <div class="field" style="left:429px;top:433px;width:167px;height:32px"></div>

  <span class="label" style="left:243px;top:476px">Phone Number *</span>
  <span class="label" style="left:429px;top:476px">Subject *</span>
  <div class="field" style="left:243px;top:490px;width:167px;height:32px"></div>
  <div class="field" style="left:429px;top:490px;width:167px;height:32px"></div>

  <span class="label" style="left:243px;top:533px">Your Message</span>
  <div class="field" style="left:243px;top:547px;width:353px;height:95px"></div>

  <div class="send">Send a Message
    <svg width="16" height="14" viewBox="0 0 16 14" fill="none" stroke="#fff" stroke-width="1.1"><path d="M1 6L15 1 11 13 7 8zM7 8l8-7M7 8v5l2-3"/></svg>
  </div>
</section>

<section class="contact-info">
  <h2 class="h2" style="left:615px;top:337px">About Information</h2>
  <div class="rule" style="left:615px;top:363px;width:344px"></div>
  <p class="about" style="left:615px;top:370px;width:346px">Lorem ipsum dolor sit amet, consectetur adipiscin Vestibulum portti egestas orci, vitae ullamcorper risus consectetur id. Donec at velit vestibulum, rutrum massa quis, porttitor lorem. Donec et ultricies arcu.Donec et ultricies arcu. In odio augue, hendrerit nec nisl ac, rhoncus gravida mauris. Quisque consectetur ligula eu urna dignissim.</p>

  <h2 class="h2" style="left:615px;top:457px">Contact Informations</h2>
  <div class="rule" style="left:615px;top:484px;width:344px"></div>

  <div class="info" style="top:505px">
    <svg width="14" height="18" viewBox="0 0 14 18" fill="none" stroke="#f2c12e" stroke-width="1.1"><path d="M7 17S1 10 1 6.5a6 6 0 0112 0C13 10 7 17 7 17z"/><circle cx="7" cy="6.5" r="2.2"/></svg>
    <span style="padding-top:3px">48 Meter Road Cabville, FA 00000</span>
  </div>
  <div class="info" style="top:545px">
    <svg width="18" height="18" viewBox="0 0 18 18" fill="none" stroke="#f2c12e" stroke-width="1.1"><path d="M3 10V8a6 6 0 0112 0v2"/><rect x="1.5" y="9" width="3" height="5" rx="1"/><rect x="13.5" y="9" width="3" height="5" rx="1"/><path d="M15 14c0 2-3 3-5 3"/></svg>
    <span style="padding-top:3px">(555) 014-3821 &nbsp;| (555) 0176-2290</span>
  </div>
  <div class="info" style="top:582px">
    <svg width="19" height="17" viewBox="0 0 19 17" fill="none" stroke="#f2c12e" stroke-width="1.1"><path d="M1 7v9h17V7L9.5 1z"/><path d="M1 16l6-5M18 16l-6-5M1 7l8.5 6L18 7M5 9V4h9v5M7 6h5M7 8h4"/></svg>
    <span style="padding-top:1px">Hello@fareline.com</span>
  </div>
  <div class="info" style="top:622px">
    <svg width="18" height="18" viewBox="0 0 18 18" fill="none" stroke="#f2c12e" stroke-width="1.1"><circle cx="9" cy="9" r="8"/><path d="M9 4v5l3 2"/></svg>
    <span>Monday - Friday: 09:00AM - 09:00PM<br>Saturday: 09:00AM - 07:00PM<br>Sunday: Closed</span>
  </div>

  <div class="follow">Follow us</div>
  <div class="social" aria-label="Social network links"><i></i><i></i><i></i><i></i><i></i></div>
</section>

<footer class="footer">
  <div class="line"></div>
  <p class="legal">© 2018 <b>Fareline.com</b> &nbsp;&nbsp;&nbsp;&nbsp;&nbsp;&nbsp;| &nbsp;Trademarks and brands are the property of their respective owners.</p>
</footer>
</body>
</html>
```